Invitation annual meeting 2017 of Corlimaux Group (2017 Annual Staff Appointments)

Version française: We want to create an invitation to the annual meeting of Groupe Corlimaux. This invitation will also be printed as a poster. You will find enclosed a photo of a "B" made with the employees of the Group during an internal event. You will absolutely have this photo on the invitation. I also send it to you when you save it while waiting for the invitation. The invitation must be festive, elegant and classy, ​​because it will take place on the 18th of December, just before Christmas (on the theme of Christmas and New Year Eve). Please, do not use the color "red" on this invitation. You can use this gray: Pantone 431 C for this invitation if you want to. The annual meeting of the staff (annual meeting) 18 December 2017 (18th) of December 2017) Halloriune (at Halloriune) From 5pm to 9.30pm (from 5pm to 9.30pm) French version: On the occasion of the annual meeting of the staff we wish to make an invitation which will also be printed as a poster. You will find in the attached elements a photo of a B made on the beach with employees. It will be necessary to use this B imperatively for your creation. I am also sending you the quick save the date we had done while waiting for the invitation. This one must be classy, ​​festive because the event will take place on December 18th, with the approach of the end-of-year celebrations (thematic New Year's Eve and non-christmas). You can use anthracite gray: Pantone 431C The group logo should appear on the invitation. Text: Annual Staff Meeting 18 December 2017 Halloriune from 5pm to 9.30pm

Project Deadline Extended Reason: Hello We give two more days on the project because we have not been fully seduced by the proposals received so far. Added Tuesday, October 24, 2017

ENG: Internal ==> employees of the Corlimaux Group FR: internal to the Group

• ENG: It is obligatory to use the photo of the "B" on the beach for this invitation. You can crop the image of the B if you want to. FR: B "made by employees" of the transmitted photo (possibility of detaching it)
• ENG: Boat photos, "kitsch" designs and the color red EN: the pictures of boats, the "kitsch", the red

```html
<!DOCTYPE html>
<html lang="fr">
<head>
<meta charset="utf-8">
<title>Rendez-vous annuel du personnel – Groupe Corlimaux</title>
<link rel="stylesheet" href="https://fonts.googleapis.com/css2?family=Cinzel&family=Tinos:wght@400;700&family=Montserrat:wght@500&display=swap">
<style>
  :root {
    --backdrop: #1d5f86;
    --paper-top: #ffffff;
    --mist: #e6ddd3;
    --sand-light: #d8c9b4;
    --sand: #c7ad86;
    --sand-deep: #a88a62;
    --sea: #a9cfcb;
    --photo-top: #b59fae;
    --photo-mid: #6f8fa6;
    --photo-low: #5d9aa8;
    --band: #0f2e38;
    --band-edge: #2b5560;
    --ink: #111111;
    --logo-ink: #3d4750;
  }
  * { margin: 0; padding: 0; box-sizing: border-box; }
  html, body {
    width: 1200px; height: 1200px; overflow: hidden;
    background: var(--backdrop);
  }
  .poster {
    position: absolute; left: 210px; top: 15px;
    width: 780px; height: 1170px; overflow: hidden;
    background: linear-gradient(180deg,
      var(--paper-top) 0px,
      var(--mist) 150px,
      var(--mist) 420px,
      var(--sea) 540px,
      var(--sea) 590px,
      var(--mist) 700px,
      var(--sand-light) 900px,
      var(--sand) 1070px);
  }
  .brand {
    position: absolute; top: 88px; left: 0; right: 0;
    padding-left: 58px;
    text-align: center;
    font-family: "Montserrat", sans-serif; font-weight: 500;
    font-size: 27px; letter-spacing: 7px;
    color: var(--logo-ink);
  }
  .staff-photo {
    position: absolute; left: 184px; top: 188px;
    width: 493px; height: 498px;
    border-radius: 24px;
    background: linear-gradient(180deg, var(--photo-top), var(--photo-mid) 50%, var(--photo-low));
    opacity: 0.85;
  }
  .details {
    position: absolute; top: 750px; left: 0; right: 0;
    text-align: center; color: var(--ink);
    font-family: "Tinos", serif; font-size: 55px; line-height: 59px;
  }
  .details .title {
    font-family: "Cinzel", serif; font-size: 52px; letter-spacing: 1px;
  }
  .details .date { font-weight: 700; font-size: 54px; }
  .footer-band {
    position: absolute; left: 0; top: 1074px; width: 100%; height: 33px;
    background: linear-gradient(180deg, var(--band-edge), var(--band) 50%, var(--band-edge));
  }
  .sand-strip {
    position: absolute; left: 0; top: 1107px; width: 100%; height: 63px;
    background: linear-gradient(180deg, var(--sand), var(--sand-deep));
  }
</style>
</head>
<body>
  <main class="poster">
    <div class="brand">GROUPE CORLIMAUX</div>

    <div class="staff-photo" role="img" aria-label="Aerial photo of the employees gathered on the beach forming the group's letter"></div>

    <div class="details">
      <div class="title">RENDEZ-VOUS</div>
      <div>annuel du personnel</div>
      <div class="date">18 Décembre 2017</div>
      <div>Au Halloriune</div>
      <div>de 17H à 21H30</div>
    </div>

    <div class="footer-band"></div>
    <div class="sand-strip"></div>
  </main>
</body>
</html>
```